Lawn sign for construction company

Would like this to be a very clean and high end design for luxury homes. We need a yard sign designed that includes the company logo, website, phone number and major service offerings (residential and commercial renovations and maintenance)
The company website is brambleworks.com all other contact info is in the attachments
Target Market(s)
Luxury home owners and business owners
Industry/Entity Type
Construction/Home Improvement
Font styles to use
Other font styles liked:
- See company logo and other graphics included for title text fonts. All other fonts can be standard sans serif.
Colors
0054AA
0677BA
7BADD7
CADEEF
E8F1F8
Requirements
Must have
- Clean, easy to read design, would like 2 sided sign. A main sign side and back side which states “free estimates, and includes the website and phone number. Must also match the color scheme of the provided logo and other company images. Dark Navy blue primary color, gray secondary color, and orange as an accent color.
Nice to have
- 2nd sign side very simple design
Should not have
- Too many graphics limit to 1-3 colors

```html
<!DOCTYPE html>
<html lang="en">
<head>
<meta charset="utf-8">
<title>Bramblewood Builders – Yard Signs</title>
<link href="https://fonts.googleapis.com/css2?family=Oswald:wght@500;600;700&display=swap" rel="stylesheet">
<style>
  :root {
    --navy: #060563;
    --orange: #e37405;
    --white: #ffffff;
    --grey: #8a8a8a;
    --backdrop: #eceef0;
  }
  * { margin: 0; padding: 0; box-sizing: border-box; }
  html, body { width: 879px; height: 1200px; overflow: hidden; }
  body { background: var(--backdrop); position: relative; font-family: "Oswald", sans-serif; }

  .sign {
    position: absolute;
    left: 172px;
    width: 537px;
    height: 376px;
    background: var(--navy);
    overflow: hidden;
  }
  .sign--front { top: 128px; }
  .sign--back { top: 727px; }

  .sign__frame {
    position: absolute;
    left: 23px; right: 23px;
    top: 23px; bottom: 0;
    border: 6px solid var(--orange);
    border-bottom: none;
  }
  .sign__band {
    position: absolute;
    left: 0; right: 0; bottom: 0;
    height: 80px;
    background: var(--orange);
    display: flex;
    align-items: center;
    justify-content: center;
  }

  .brand {
    position: absolute;
    left: 0; right: 0;
    display: flex;
    align-items: center;
    justify-content: center;
    gap: 10px;
    color: var(--white);
    font-weight: 600;
    letter-spacing: 1px;
    text-transform: uppercase;
    line-height: 1;
  }
  .brand__dot {
    border-radius: 50%;
    background: var(--grey);
    flex: none;
  }
  .sign--front .brand { top: 122px; font-size: 34px; }
  .sign--front .brand__dot { width: 30px; height: 30px; }
  .sign--back .brand { top: 196px; font-size: 24px; }
  .sign--back .brand__dot { width: 22px; height: 22px; }

  .contact {
    position: absolute;
    left: 0; right: 0;
    display: flex;
    justify-content: center;
    align-items: center;
    gap: 16px;
    color: var(--white);
    font-weight: 600;
    font-size: 28px;
    line-height: 1;
  }
  .contact__item { display: flex; align-items: center; gap: 4px; }
  .contact__icon { width: 20px; height: 20px; flex: none; }
  .sign--front .contact { top: 261px; }
  .sign--back .contact { top: 321px; }

  .tagline {
    color: var(--white);
    font-weight: 600;
    font-size: 22px;
    line-height: 25px;
    text-align: center;
    text-transform: uppercase;
    letter-spacing: 0.6px;
  }

  .headline {
    position: absolute;
    left: 0; right: 0;
    top: 59px;
    text-align: center;
    color: var(--orange);
    font-weight: 700;
    font-size: 64px;
    line-height: 1;
    letter-spacing: 0;
  }
</style>
</head>
<body>

<svg width="0" height="0" style="position:absolute">
  <defs>
    <symbol id="icon-phone" viewBox="0 0 24 24">
      <path d="M6.6 3.5l2.6 3.4-1.6 2.2c.9 2.2 2.9 4.3 5.2 5.3l2.2-1.6 3.5 2.6-1.1 3.3c-.3.6-1 .9-1.7.8C9.3 18.6 5.4 14.7 4.4 8.3c-.1-.7.2-1.4.8-1.7z" fill="none" stroke="#fff" stroke-width="1.6" stroke-linejoin="round"/>
      <path d="M14 4.5a6 6 0 0 1 5.5 5.5M14 7.5a3 3 0 0 1 2.5 2.5" fill="none" stroke="#fff" stroke-width="1.4" stroke-linecap="round"/>
    </symbol>
    <symbol id="icon-globe" viewBox="0 0 24 24">
      <circle cx="12" cy="12" r="9.5" fill="none" stroke="#fff" stroke-width="1.4"/>
      <ellipse cx="12" cy="12" rx="4.2" ry="9.5" fill="none" stroke="#fff" stroke-width="1.2"/>
      <path d="M2.5 12h19M4 7h16M4 17h16" fill="none" stroke="#fff" stroke-width="1.1"/>
    </symbol>
  </defs>
</svg>

<section class="sign sign--front" aria-label="Front of sign">
  <div class="sign__frame"></div>
  <div class="brand"><span class="brand__dot"></span><span class="brand__name">Bramblewood Builders</span></div>
  <div class="contact">
    <span class="contact__item"><svg class="contact__icon"><use href="#icon-phone"/></svg>1 555-204-7316</span>
    <span class="contact__item"><svg class="contact__icon"><use href="#icon-globe"/></svg>brambleworks.com</span>
  </div>
  <div class="sign__band">
    <p class="tagline">Residential and commercial renovations<br>and maintenance</p>
  </div>
</section>

<section class="sign sign--back" aria-label="Back of sign">
  <div class="sign__frame"></div>
  <h1 class="headline">FREE ESTIMATES</h1>
  <div class="brand"><span class="brand__dot"></span><span class="brand__name">Bramblewood Builders</span></div>
  <div class="sign__band"></div>
  <div class="contact">
    <span class="contact__item"><svg class="contact__icon"><use href="#icon-phone"/></svg>1 555-204-7316</span>
    <span class="contact__item"><svg class="contact__icon"><use href="#icon-globe"/></svg>brambleworks.com</span>
  </div>
</section>

</body>
</html>
```